Service Plan Sales Flyer

The Watchpost Depot (www.kelvamart.com) is a commercial security integrator that installs security cameras, access control, intrusion, two-way radios and perimeter security. We require a one page flyer for our service plan for new and existing customers. The price of the service plan is $299/yr and includes the following;
1. Discounted service rate of $118/hr
2. Free remote support ($85/hr without a plan)
3. Free remote training
4. Priority support

Please review our brochure attached and create a one page sales flyer with the end goal of having the client sign up for our annual service plan . The plan will automatically renew every year. Email sales@kelvamart.com.

Target Market(s)

commercial industrial clients - no residential

Industry/Entity Type

review our website at www.kelvamart.com

Colors
0054AA
0677BA
7BADD7
CADEEF
E8F1F8
EE7325
F08F49
F5BC92
FAE3D3
FDF4ED

Requirements
Must have
• call to action
Should not have
• too many colors

```html
<!DOCTYPE html>
<html lang="en">
<head>
<meta charset="utf-8">
<title>The Watchpost Depot – Service Plan Flyer</title>
<link rel="stylesheet" href="https://fonts.googleapis.com/css2?family=Oswald:wght@500;700&family=Open+Sans:wght@400;600&display=swap">
<style>
  :root {
    --navy: #132b5c;
    --red: #e0352d;
    --white: #ffffff;
    --ink: #2a2a2a;
    --leaf: #8fae4a;
    --leaf-light: #d8e6b8;
    --frame-grey: #e4e7ec;
  }
  * { margin: 0; padding: 0; box-sizing: border-box; }
  html, body { width: 900px; height: 1200px; overflow: hidden; background: var(--white); }
  .flyer { position: relative; width: 900px; height: 1200px; background: var(--white); overflow: hidden; font-family: "Open Sans", Arial, sans-serif; }

  .stripe { position: absolute; }
  .stripe--top-navy { left: 460px; top: 48px; width: 440px; height: 22px; background: var(--navy); clip-path: polygon(3% 0, 100% 0, 100% 100%, 0 100%); }
  .stripe--top-red { left: 0; top: 70px; width: 480px; height: 14px; background: var(--red); clip-path: polygon(0 0, 100% 0, 98% 100%, 0 100%); }
  .stripe--photo-navy { left: 0; top: 480px; width: 900px; height: 16px; background: var(--navy); }

  .hero-photo { position: absolute; left: 0; top: 84px; width: 900px; height: 396px;
    background:
      linear-gradient(90deg, rgba(255,255,255,0) 0%, rgba(255,255,255,0) 40%, rgba(255,255,255,.85) 58%, #fff 75%),
      radial-gradient(ellipse at 30% 40%, var(--leaf-light) 0%, var(--leaf) 55%, #5f7d33 100%); }

  .brand { position: absolute; left: 505px; top: 170px; display: flex; align-items: center; gap: 14px; }
  .brand__mark { width: 34px; height: 34px; background: var(--navy); }
  .brand__name { font-family: "Oswald", Arial, sans-serif; font-weight: 700; font-size: 30px; line-height: 1; color: var(--navy); text-transform: uppercase; }
  .brand__tagline { position: absolute; left: 553px; top: 212px; font-family: "Open Sans", Arial, sans-serif; font-weight: 600; font-size: 12px; color: var(--red); }

  .plan-panel { position: absolute; left: 510px; top: 350px; width: 370px; height: 480px; background: var(--red); color: var(--white); padding: 26px 24px 0 28px; }
  .plan-panel__heading { font-family: "Oswald", Arial, sans-serif; font-weight: 700; text-align: center; text-transform: uppercase; line-height: 1.08; }
  .plan-panel__line { display: block; font-size: 42px; }
  .plan-panel__price { display: block; font-size: 52px; }
  .plan-panel__includes { display: block; font-size: 40px; text-transform: none; }
  .plan-panel__arrow { display: block; margin: 2px auto 14px; }
  .plan-list { list-style: none; }
  .plan-list__item { display: flex; align-items: flex-start; gap: 12px; font-size: 19px; line-height: 1.25; margin-bottom: 22px; }
  .plan-list__tick { flex: none; width: 30px; height: 30px; }

  .headline { position: absolute; left: 30px; top: 526px; width: 460px; font-family: "Oswald", Arial, sans-serif; font-weight: 700; text-align: center; text-transform: uppercase; line-height: 1.1; }
  .headline__primary { display: block; font-size: 62px; color: var(--navy); letter-spacing: -0.5px; }
  .headline__secondary { display: block; font-size: 52px; color: var(--red); }
  .headline__divider { color: var(--navy); }

  .intro { position: absolute; left: 32px; top: 690px; width: 450px; font-size: 14px; line-height: 1.45; color: var(--ink); text-align: justify; }
  .intro p + p { margin-top: 16px; }

  .product-grid { position: absolute; left: 37px; top: 870px; width: 448px; height: 292px; background: var(--navy); padding: 22px; display: grid; grid-template-columns: 1fr 1fr; grid-template-rows: 1fr 1fr; gap: 6px; }
  .product-grid__cell { background: linear-gradient(135deg, #f4f5f7, #c9ced6); }
  .product-grid__cell--dark { background: linear-gradient(135deg, #eef0f3, #555a62); }

  .contact { position: absolute; left: 518px; top: 858px; width: 350px; text-align: center; }
  .contact__cta { font-family: "Oswald", Arial, sans-serif; font-weight: 700; font-size: 50px; color: var(--navy); line-height: 1.1; text-transform: uppercase; }
  .contact__phone { font-family: "Oswald", Arial, sans-serif; font-weight: 700; font-size: 48px; color: var(--red); line-height: 1.05; }
  .contact__address { font-size: 13px; color: var(--ink); margin-top: 6px; }
  .contact__hours { margin-top: 10px; background: var(--navy); color: var(--white); font-weight: 600; font-size: 19px; padding: 3px 0; }

  .web-band { position: absolute; left: 480px; top: 1100px; width: 420px; height: 62px; background: var(--red); clip-path: polygon(6% 0, 100% 0, 100% 100%, 0 100%); color: var(--white); font-size: 19px; letter-spacing: 2px; display: flex; align-items: center; justify-content: center; padding-left: 40px; }
  .stripe--bottom-red { left: 0; top: 1178px; width: 490px; height: 10px; background: var(--red); }
</style>
</head>
<body>
<main class="flyer">
  <div class="stripe stripe--top-navy"></div>
  <div class="stripe stripe--top-red"></div>

  <div class="hero-photo" role="img" aria-label="Photo of a white outdoor security camera on a wall bracket against blurred green foliage"></div>

  <div class="brand">
    <span class="brand__mark"></span>
    <span class="brand__name">The Watchpost Depot</span>
  </div>
  <div class="brand__tagline">Commercial &amp; Industrial Solutions</div>

  <div class="stripe stripe--photo-navy"></div>

  <section class="plan-panel">
    <h2 class="plan-panel__heading">
      <span class="plan-panel__line">Service plan is</span>
      <span class="plan-panel__price">$299/YR</span>
      <span class="plan-panel__includes">includes</span>
    </h2>
    <svg class="plan-panel__arrow" width="16" height="22" viewBox="0 0 16 22" aria-hidden="true">
      <path d="M8 0v18M2 12l6 7 6-7" fill="none" stroke="#fff" stroke-width="2.5"/>
    </svg>
    <ul class="plan-list">
      <li class="plan-list__item">
        <svg class="plan-list__tick" viewBox="0 0 30 30" aria-hidden="true"><rect x="1" y="3" width="26" height="26" fill="#fff"/><path d="M6 15l6 7L28 2" fill="none" stroke="#132b5c" stroke-width="4"/></svg>
        <span>Discounted service rate of $118/hr</span>
      </li>
      <li class="plan-list__item">
        <svg class="plan-list__tick" viewBox="0 0 30 30" aria-hidden="true"><rect x="1" y="3" width="26" height="26" fill="#132b5c"/><path d="M6 15l6 7L28 2" fill="none" stroke="#e0352d" stroke-width="4"/></svg>
        <span>Free remote support<br>($85/hr without a plan)</span>
      </li>
      <li class="plan-list__item">
        <svg class="plan-list__tick" viewBox="0 0 30 30" aria-hidden="true"><rect x="1" y="3" width="26" height="26" fill="#fff"/><path d="M6 15l6 7L28 2" fill="none" stroke="#132b5c" stroke-width="4"/></svg>
        <span>Free remote training</span>
      </li>
      <li class="plan-list__item">
        <svg class="plan-list__tick" viewBox="0 0 30 30" aria-hidden="true"><rect x="1" y="3" width="26" height="26" fill="#132b5c"/><path d="M6 15l6 7L28 2" fill="none" stroke="#e0352d" stroke-width="4"/></svg>
        <span>Priority support</span>
      </li>
    </ul>
  </section>

  <h1 class="headline">
    <span class="headline__primary">Knowledgeable</span>
    <span class="headline__secondary">Reliable <span class="headline__divider">|</span> Easy</span>
  </h1>

  <div class="intro">
    <p>From it's humble beginning in 1999, The Watchpost Depot Employees have worked hard to become one of Canada's most trusted commercial security integrators.</p>
    <p>We started 20 years ago when businesses still used VCR tapes to record their terrible grainy video for the entire day. Now we are called on by the smartest clients (that's you) to install high definition camera systems, card swipe access control, alarm systems and intercoms … all accessible on their phones, tablets and PC</p>
  </div>

  <div class="product-grid">
    <div class="product-grid__cell" role="img" aria-label="Photo of a hand holding a key fob to a wall-mounted card reader"></div>
    <div class="product-grid__cell" role="img" aria-label="Screenshot of access control software windows"></div>
    <div class="product-grid__cell product-grid__cell--dark" role="img" aria-label="Photo of a black electronic door lock device"></div>
    <div class="product-grid__cell" role="img" aria-label="Photo of a video monitor, intercom panels and a security camera"></div>
  </div>

  <section class="contact">
    <h2 class="contact__cta">Call us today</h2>
    <p class="contact__phone">1-877-555-0142</p>
    <p class="contact__address">#14, 2870 Alderwood Way SE Calgary, AB T2C 4K1</p>
    <p class="contact__hours">Monday to Friday 8 AM - 5 PM</p>
  </section>

  <div class="web-band">www.kelvamart.com</div>
  <div class="stripe stripe--bottom-red"></div>
</main>
</body>
</html>
```